Website design to promote trampoline business

We require a website design for our business. The business is primarily provising access for people between 5YO and 40YO to jump on trampolines for fun and fitness.

We have a logo and color schemes already and the website should incorporate these colors and designs.

We would like to incorporate the following pages:-

Book Now!
Home
About Us
Locations & Hours
Jumping
Groups & Events
Gallery
Safety
Latest News
Careers

Industry/Entity Type

Business

Requirements
Must have
• Incorporate our logo and colors (files attached).

```html
<!DOCTYPE html>
<html lang="en">
<head>
<meta charset="utf-8">
<title>Bouncely – Trampoline Park</title>
<link href="https://fonts.googleapis.com/css2?family=Open+Sans:wght@400;600;700;800&display=swap" rel="stylesheet">
<style>
:root{
  --orange:#f39a1e;
  --blue:#3f8fd6;
  --blue-dark:#2c6fb0;
  --nav:#3b3b3b;
  --ink:#333;
  --muted:#777;
  --panel:#dcdcdc;
  --panel-2:#ececec;
  --card-grey:#a3a3a3;
  --footer:#2f2f2f;
  --white:#fff;
}
*{box-sizing:border-box;margin:0;padding:0}
html,body{width:682px;height:1200px;overflow:hidden}
body{font-family:"Open Sans",Arial,sans-serif;color:var(--ink);background:var(--panel-2);font-size:7px;line-height:1.4}
.wrap{width:480px;margin:0 auto;position:relative}

/* header */
.site-header{height:68px;background:var(--white)}
.site-header .wrap{height:68px}
.brand{position:absolute;left:0;top:12px;display:flex;align-items:center;gap:6px;font-weight:800;font-size:24px;color:var(--blue);letter-spacing:1px}
.brand-mark{width:14px;height:14px;background:var(--orange)}
.search{position:absolute;right:0;top:38px;width:150px;height:20px;border:1px solid #ccc;font-size:7px;color:#aaa;padding:5px 6px}
.search svg{position:absolute;right:5px;top:5px}

/* nav */
.main-nav{height:24px;background:var(--nav)}
.main-nav ul{list-style:none;display:flex;height:24px}
.main-nav li{color:#eee;font-size:7.5px;padding:0 8px;line-height:24px;white-space:nowrap}
.main-nav li.active{background:var(--orange);color:var(--white);font-weight:700}

/* hero */
.hero{height:218px;background:var(--panel)}
.hero-slide{position:relative;height:218px;background:linear-gradient(180deg,#7fa664 0%,#5e8a45 45%,#4d7b3a 70%,#6a8f55 100%)}
.hero-caption{position:absolute;left:22px;top:140px}
.hero-caption h2{background:rgba(30,30,30,.75);color:var(--white);font-size:14px;font-weight:700;padding:5px 9px}
.btn-book{display:inline-block;margin-top:6px;margin-left:10px;background:var(--blue);color:var(--white);font-size:7px;font-weight:700;padding:5px 12px}
.arrow{position:absolute;top:98px;width:14px;height:18px;background:rgba(0,0,0,.45)}
.arrow.prev{left:0}.arrow.next{right:0}
.thumbs{position:absolute;right:12px;bottom:8px;display:flex;gap:4px}
.thumbs span{width:40px;height:24px;border:2px solid var(--white);background:#6d8f58}
.thumbs span:first-child{border-color:var(--orange)}

/* offers */
.offers{height:230px;background:var(--panel);padding-top:10px}
.section-title{display:flex;align-items:center;gap:10px;justify-content:center;font-size:8px;font-weight:700;letter-spacing:1px;color:#444}
.section-title::before,.section-title::after{content:"";width:150px;height:1px;background:#aaa}
.offer-cards{display:flex;justify-content:space-between;margin-top:14px;padding:0 17px}
.offer{width:122px;height:182px;background:var(--card-grey);padding:7px;color:var(--white);text-align:center}
.offer.featured{background:var(--blue)}
.offer-img{height:62px;background:linear-gradient(180deg,#9cc27a,#4d7d3b);border:2px solid var(--white)}
.offer h3{font-size:7px;font-weight:700;margin:8px 0 4px}
.offer p{font-size:6px;line-height:1.5}
.read-more{display:inline-block;margin-top:10px;background:#444;color:var(--white);font-size:6px;font-weight:700;padding:4px 10px}

/* welcome */
.welcome{height:122px;background:var(--white);padding-top:12px}
.welcome .wrap{display:flex;gap:12px}
.welcome-img{width:125px;height:98px;background:linear-gradient(180deg,#7fb0d8,#d79bb5)}
.welcome h2{font-size:13px;font-weight:800;color:#222}
.welcome h4{font-size:7px;color:var(--blue);font-weight:700;margin:3px 0 5px}
.welcome p{font-size:6px;color:var(--muted);width:340px}

/* columns */
.columns{height:305px;padding-top:14px}
.columns .wrap{display:flex;justify-content:space-between}
.col h3{font-size:8px;font-weight:700;letter-spacing:.5px;border-bottom:1px solid #bbb;padding-bottom:4px;margin-bottom:8px}
.col-new{width:128px}
.product{display:flex;gap:6px;margin-bottom:12px;align-items:center}
.product-img{width:56px;height:42px;background:radial-gradient(ellipse at center,#3b5fa8 40%,#eaeaea 42%)}
.date{display:inline-block;background:var(--blue);color:var(--white);font-size:5.5px;padding:1px 5px;margin-bottom:3px}
.product .name{font-size:7px;color:#444}
.col-safety{width:140px;background:#cfcfcf;padding:8px;height:270px}
.col-safety ul{list-style:none}
.col-safety li{display:flex;gap:5px;align-items:center;font-size:6px;color:#555;padding:8px 0;border-bottom:1px solid #bdbdbd}
.tick{width:8px;height:8px;background:var(--white);border:1px solid #999}
.col-news{width:160px}
.news{display:flex;gap:6px;margin-bottom:12px}
.news-img{width:46px;height:38px;background:linear-gradient(180deg,#88b570,#c98a3e)}
.news p{font-size:6.5px;color:var(--orange);font-weight:600}
.news .when{color:var(--blue);font-size:5.5px;font-weight:400}

/* gallery & events */
.gallery-band{height:155px;background:#c9c9c9;padding-top:12px}
.gallery-band .wrap{display:flex;justify-content:space-between}
.gallery{width:290px}
.gallery h3,.events h3{font-size:8px;font-weight:700;margin-bottom:8px;display:flex;justify-content:space-between}
.gallery h3 span{font-size:6px;color:var(--blue);font-weight:400}
.gallery-grid{display:grid;grid-template-columns:repeat(4,66px);gap:8px}
.gallery-grid div{height:46px;border:2px solid var(--white)}
.g1{background:linear-gradient(#7db2e0,#5d8f3e)}.g2{background:linear-gradient(#c4463c,#5b7fbf)}
.g3{background:linear-gradient(#e0c24a,#4d7d3b)}.g4{background:linear-gradient(#7d58a8,#3c5fa8)}
.g5{background:linear-gradient(#8ec3e8,#2e6ab0)}.g6{background:linear-gradient(#6aa0d8,#e07c3a)}
.g7{background:linear-gradient(#7aa85a,#3c5f8f)}.g8{background:linear-gradient(#a7c8e8,#3b4f8f)}
.events{width:150px;background:#dadada;padding:8px;height:140px;margin-top:-4px}
.event{display:flex;gap:6px;margin-bottom:7px;align-items:center}
.event-date{width:30px;height:26px;background:var(--blue);color:var(--white);font-size:6px;font-weight:700;text-align:center;padding-top:3px;line-height:1.3}
.event p{font-size:6px;color:#555}
.spacer{height:26px;background:#dedede}

/* footer */
.site-footer{height:54px;background:var(--footer);color:#bbb;padding-top:14px}
.site-footer .links{font-size:6.5px;color:#ddd}
.site-footer .copy{font-size:5.5px;margin-top:3px}
.social{position:absolute;right:10px;top:0;display:flex;gap:6px}
.social span{width:16px;height:16px;border-radius:50%;background:var(--blue)}
</style>
</head>
<body>
<header class="site-header">
  <div class="wrap">
    <div class="brand"><span class="brand-mark"></span>BOUNCELY</div>
    <div class="search">Search
      <svg width="9" height="9" viewBox="0 0 10 10"><circle cx="4" cy="4" r="3" fill="none" stroke="#999" stroke-width="1.3"/><line x1="6.3" y1="6.3" x2="9" y2="9" stroke="#999" stroke-width="1.3"/></svg>
    </div>
  </div>
</header>

<nav class="main-nav">
  <div class="wrap">
    <ul>
      <li class="active">Home</li><li>About Us</li><li>Locations &amp; Hours</li><li>Jumping</li><li>Groups &amp; Events</li><li>Gallery</li><li>Safety</li><li>Latest News</li><li>Careers</li>
    </ul>
  </div>
</nav>

<section class="hero">
  <div class="wrap hero-slide" role="img" aria-label="Family jumping on a backyard trampoline on a green lawn">
    <span class="arrow prev"></span><span class="arrow next"></span>
    <div class="hero-caption">
      <h2>DARE TO FLY HIGHER!</h2>
      <span class="btn-book">BOOK NOW</span>
    </div>
    <div class="thumbs"><span></span><span></span><span></span><span></span></div>
  </div>
</section>

<section class="offers">
  <div class="wrap">
    <h2 class="section-title">WHAT WE OFFER</h2>
    <div class="offer-cards">
      <article class="offer featured">
        <div class="offer-img" role="img" aria-label="Trampoline on grass"></div>
        <h3>INTERIUM MALESUADA</h3>
        <p>Jump sessions for all ages with safe nets, soft pads and trained staff on every court.</p>
        <span class="read-more">READ MORE</span>
      </article>
      <article class="offer">
        <div class="offer-img" role="img" aria-label="Round trampoline in a garden"></div>
        <h3>INTERIUM MALESUADA</h3>
        <p>Fitness classes that turn every bounce into a full body workout for teens and adults.</p>
        <span class="read-more">READ MORE</span>
      </article>
      <article class="offer">
        <div class="offer-img" role="img" aria-label="Trampoline with safety padding"></div>
        <h3>INTERIUM MALESUADA</h3>
        <p>Private parties and group events with reserved courts, snacks and a party host.</p>
        <span class="read-more">READ MORE</span>
      </article>
    </div>
  </div>
</section>

<section class="welcome">
  <div class="wrap">
    <div class="welcome-img" role="img" aria-label="Child smiling in a play area"></div>
    <div>
      <h2>WELCOME</h2>
      <h4>INTERIUM ET MALESUADA FAMES AC ANTE IPSUM PRIMIS IN FAUCIBUS. UT IN NISI AC SOLLICITUDIN.</h4>
      <p>Our park opens its doors to jumpers aged five to forty who want fun, fitness and fresh air in one place. Choose open jump, join a class or bring your friends for a party. Every court is checked daily, every session is supervised and every visit ends with a smile. Book your time online, grab your grip socks and get ready to fly higher than ever before with us.</p>
    </div>
  </div>
</section>

<section class="columns">
  <div class="wrap">
    <div class="col col-new">
      <h3>WHAT'S NEW?</h3>
      <div class="product"><div class="product-img" role="img" aria-label="Round trampoline"></div><div><span class="date">Mar 12, 2014</span><div class="name">Model Name</div></div></div>
      <div class="product"><div class="product-img" role="img" aria-label="Round trampoline"></div><div><span class="date">Mar 12, 2014</span><div class="name">Model Name</div></div></div>
      <div class="product"><div class="product-img" role="img" aria-label="Round trampoline"></div><div><span class="date">Mar 12, 2014</span><div class="name">Model Name</div></div></div>
    </div>
    <div class="col col-safety">
      <h3>SAFETY</h3>
      <ul>
        <li><span class="tick"></span>Always jump one at a time</li>
        <li><span class="tick"></span>Wear grip socks on courts</li>
        <li><span class="tick"></span>No flips without a coach</li>
        <li><span class="tick"></span>Empty pockets before jumping</li>
        <li><span class="tick"></span>Follow staff instructions</li>
      </ul>
    </div>
    <div class="col col-news">
      <h3>OUR LATEST NEWS</h3>
      <div class="news"><div class="news-img" role="img" aria-label="Kids on trampoline"></div><div><p>New dodgeball court opens this spring</p><span class="when">Mar 12, 2014</span></div></div>
      <div class="news"><div class="news-img" role="img" aria-label="Trampoline park hall"></div><div><p>Teen fitness nights every Friday</p><span class="when">Mar 12, 2014</span></div></div>
      <div class="news"><div class="news-img" role="img" aria-label="Jumping group"></div><div><p>Holiday camps now open to book</p><span class="when">Mar 12, 2014</span></div></div>
    </div>
  </div>
</section>

<section class="gallery-band">
  <div class="wrap">
    <div class="gallery">
      <h3>GALLERY <span>View More</span></h3>
      <div class="gallery-grid">
        <div class="g1" role="img" aria-label="Outdoor trampoline"></div>
        <div class="g2" role="img" aria-label="Indoor jump court"></div>
        <div class="g3" role="img" aria-label="Kids bouncing"></div>
        <div class="g4" role="img" aria-label="Trampoline frame"></div>
        <div class="g5" role="img" aria-label="Jumper in the air"></div>
        <div class="g6" role="img" aria-label="Party group"></div>
        <div class="g7" role="img" aria-label="Garden trampoline"></div>
        <div class="g8" role="img" aria-label="Round trampoline"></div>
      </div>
    </div>
    <div class="events">
      <h3>UPCOMING EVENTS</h3>
      <div class="event"><div class="event-date">12<br>MAR</div><p>Family jump day with prizes</p></div>
      <div class="event"><div class="event-date">20<br>MAR</div><p>Fitness bootcamp for adults</p></div>
      <div class="event"><div class="event-date">28<br>MAR</div><p>Glow night open session</p></div>
    </div>
  </div>
</section>
<div class="spacer"></div>

<footer class="site-footer">
  <div class="wrap">
    <div class="links">Home | Locations &amp; Hours | Jumping | Safety | Careers | Contact</div>
    <div class="copy">Copyright © 2014 Bouncely. All rights reserved.</div>
    <div class="social"><span></span><span></span><span></span><span></span></div>
  </div>
</footer>
</body>
</html>
```